Box design for Jade Roller and gua sha set

Hello I am looking to have a box designed for a Jade Roller and gua sha set. The dimensions have already been Determined. There will be 3 sides with design, 2 sides on the outside with design and 1 on the inside of the box for instructions.

I have attached an Ai file that has the exact dimensions of the box.
I have also attached a few pictures of my product, please find the best way to use them on the box design along with my logos (which I will also attach).

The title of the product is "Jade Roller & Gua Sha Set".

The brand for this product is Willowmere Goods (please use the logo provided)

I have attached a second logo that says "Brinvale, Willowmere Goods...Willowmere Goods is a part of the Brinvale Group" Please put this somewhere on the back side of the packaging (preferably at the bottom right corner, small)
Also on the back side please neatly place these features:
SUPERIOR QUALITY: Made from real Jade Stone and developed with high quality materials which result in smooth, noise free rolling
BLOOD CIRCULATION: The Jade Roller has two sides, the bigger side for the general facial area and the smaller side for more accurate massaging around the eyes
ROLL AWAY AGE AND PUFFY DARK EYES: This roller will reduce the dark circles and puffiness around your eyes by circulating blood flow which allows more blood cells to get to places which is difficult without rolling. It will also help reduce the appearance of wrinkles on the forehead with the same method.
GUA SHA TOOL: Included is a Gua Sha tool which is very effective for eye massaging, facial lifting and body scraping
VELVET TRAVEL BAG: Included is also a small carrying bag for the roller and gua sha that tightens

For the inside of the box please insert the instructions photo I have provided. I want to be able to edit the words in this after so please make sure I can do that in adobe.

```html
<!DOCTYPE html>
<html lang="en">
<head>
<meta charset="utf-8">
<title>Jade Roller &amp; Gua Sha Set – Box Dieline</title>
<link rel="stylesheet" href="https://fonts.googleapis.com/css2?family=Kaushan+Script&family=Open+Sans:wght@400;700&family=Oswald:wght@300;400&display=swap">
<style>
  :root {
    --backdrop: #3f5235;
    --teal: #5cc4c6;
    --teal-deep: #2b9d99;
    --teal-pattern: #4fb6b8;
    --panel-white: #ffffff;
    --panel-soft: #f3f6f6;
    --ink: #1d1d1d;
    --jade: #b9dcb4;
    --jade-deep: #8cc08a;
    --dieline: #e8efe6;
  }
  html, body {
    margin: 0;
    padding: 0;
    width: 1200px;
    height: 960px;
    overflow: hidden;
    background: var(--backdrop);
  }
  .dieline {
    position: absolute;
    left: 326px;
    top: 37px;
    width: 548px;
    height: 885px;
  }
  .cut-line { fill: none; stroke: var(--dieline); stroke-width: 1.2; }
  .panel-white { fill: var(--panel-white); }
  .panel-soft { fill: var(--panel-soft); }
  .band { fill: var(--teal); }
  .band-label {
    font-family: "Oswald", sans-serif;
    font-weight: 300;
    font-size: 31px;
    fill: #ffffff;
    text-anchor: middle;
  }
  .script-title {
    font-family: "Kaushan Script", cursive;
    fill: var(--teal-deep);
    text-anchor: middle;
  }
  .feature {
    font-family: "Open Sans", sans-serif;
    font-size: 10.6px;
    fill: var(--teal-deep);
  }
  .feature .lead { font-weight: 700; }
  .brand-name {
    font-family: "Open Sans", sans-serif;
    font-weight: 700;
    fill: var(--ink);
  }
  .title-box { fill: var(--teal); stroke: var(--panel-white); stroke-width: 4; }
  .title-inner { fill: none; stroke: var(--panel-white); stroke-width: 2; }
  .title-main {
    font-family: "Oswald", sans-serif;
    font-weight: 300;
    font-size: 58px;
    fill: #ffffff;
    text-anchor: middle;
    letter-spacing: 1px;
  }
  .title-sub {
    font-family: "Kaushan Script", cursive;
    font-size: 29px;
    fill: #ffffff;
    text-anchor: middle;
  }
  .brand-mark { fill: #d8343a; }
</style>
</head>
<body>
<svg class="dieline" viewBox="0 0 685 1106" xmlns="http://www.w3.org/2000/svg">
  <!-- outer cut line -->
  <polygon class="cut-line" points="80,0 606,0 685,78 685,1030 606,1106 80,1106 0,1030 0,78"/>

  <!-- back panel (printed upside down on the flat) -->
  <rect class="panel-white" x="45" y="46" width="595" height="400"/>
  <g class="back-panel" transform="rotate(180 342.5 246) translate(45 46)">
    <text class="script-title" x="297" y="60" font-size="26">Jade Roller &amp; Gua Sha Set</text>

    <text class="feature" x="50" y="94"><tspan class="lead">SUPERIOR QUALITY:</tspan> Made from real Jade Stone and developed with high quality</text>
    <text class="feature" x="50" y="109">materials which result in smooth, noise free rolling</text>

    <text class="feature" x="50" y="140"><tspan class="lead">BLOOD CIRCULATION:</tspan> The Jade Roller has two sides, the bigger side for the general</text>
    <text class="feature" x="50" y="155">facial area and the smaller side for more accurate massaging around the eyes</text>

    <text class="feature" x="50" y="186"><tspan class="lead">ROLL AWAY AGE AND PUFFY DARK EYES:</tspan> This roller will reduce the dark circles and</text>
    <text class="feature" x="50" y="201">puffiness around your eyes by circulating blood flow which allows more blood cells</text>
    <text class="feature" x="50" y="216">to get to places which is difficult without rolling. It will also help reduce the appear</text>
    <text class="feature" x="50" y="231">ance of wrinkles on the forehead with the same method.</text>

    <text class="feature" x="50" y="262"><tspan class="lead">GUA SHA TOOL:</tspan> Included is a Gua Sha tool which is very effective for eye massaging,</text>
    <text class="feature" x="50" y="277">facial lifting and body scraping</text>

    <text class="feature" x="50" y="308"><tspan class="lead">VELVET TRAVEL BAG:</tspan> Included is also a small carrying bag for the roller and gua sha</text>
    <text class="feature" x="50" y="323">that tightens</text>

    <g class="group-brand">
      <circle class="brand-mark" cx="392" cy="346" r="5"/>
      <text class="brand-name" x="401" y="349" font-size="7">WILLOWMERE GOODS</text>
      <text class="brand-name" x="388" y="370" font-size="18" letter-spacing="1">BRINVALE</text>
    </g>
  </g>

  <!-- top spine band -->
  <rect class="band" x="45" y="456" width="595" height="85"/>
  <text class="band-label" x="342.5" y="498" transform="rotate(180 342.5 498)" dy="11">Jade Roller &amp; Gua Sha Set</text>

  <!-- front panel -->
  <rect class="panel-soft" x="45" y="551" width="595" height="400" role="img" aria-label="Faint light-grey geometric lattice pattern"/>
  <rect x="45" y="551" width="595" height="200" fill="var(--teal-pattern)" role="img" aria-label="Teal geometric lattice pattern band"/>

  <rect class="title-box" x="172" y="639" width="344" height="122"/>
  <rect class="title-inner" x="180" y="647" width="328" height="106"/>
  <text class="title-main" x="344" y="704">JADE ROLLER</text>
  <text class="title-sub" x="344" y="742">&amp; Gua Sha Set</text>

  <rect x="162" y="774" width="355" height="108" rx="40" fill="var(--jade)" role="img" aria-label="Product image of the jade gua sha stone and double-ended jade roller"/>

  <g class="front-brand">
    <circle class="brand-mark" cx="297" cy="903" r="14"/>
    <text class="brand-name" x="320" y="900" font-size="14" fill="var(--ink)">WILLOWMERE</text>
    <text class="brand-name" x="320" y="915" font-size="14" fill="var(--ink)">GOODS</text>
  </g>

  <!-- bottom spine band -->
  <rect class="band" x="45" y="961" width="595" height="85"/>
  <text class="band-label" x="342.5" y="1014">Jade Roller &amp; Gua Sha Set</text>
</svg>
</body>
</html>
```